KV MOTORS BANNER/SIGN DESIGN

Design a banner sign for outdoor use for KV MOTORS - a premium pre owned vehicle sales center. The size must be 36 feet in width
and 3 feet in height.

Information required: logo (attached)
-PREMIUM PRE-OWEND VEHICLE SALES
- 403.555.0172

perhaps in smaller font: BUY-SELL-TRADE

prefer white background but could possibly do red matching the logo

```html
<!DOCTYPE html>
<html lang="en">
<head>
<meta charset="utf-8">
<title>KV Motors Banner</title>
<link rel="stylesheet" href="https://fonts.googleapis.com/css2?family=Poppins:wght@400;600;700;800&display=swap">
<style>
  :root {
    --red: #d0101a;
    --red-dark: #6a0408;
    --ink: #1e1e1e;
    --paper: #ffffff;
    --photo-light: #f2f2f2;
    --photo-mid: #d9d9d9;
  }
  * { margin: 0; padding: 0; box-sizing: border-box; }
  html, body { width: 1200px; height: 100px; overflow: hidden; background: var(--paper); }
  .banner {
    position: relative;
    width: 1200px;
    height: 100px;
    background: var(--paper);
    font-family: "Poppins", sans-serif;
    color: var(--ink);
    overflow: hidden;
  }
  .banner__shapes { position: absolute; inset: 0; }
  .brand {
    position: absolute;
    left: 361px;
    top: 23px;
    height: 56px;
    display: flex;
    align-items: center;
    gap: 14px;
  }
  .brand__dot {
    width: 56px;
    height: 56px;
    border-radius: 50%;
    border: 5px solid var(--red);
  }
  .brand__name {
    font-weight: 800;
    font-size: 30px;
    letter-spacing: 1px;
    color: var(--ink);
    line-height: 1;
  }
  .tagline {
    position: absolute;
    left: 639px;
    top: 20px;
    font-size: 20.5px;
    font-weight: 400;
    line-height: 1;
    letter-spacing: 0.1px;
  }
  .phone {
    position: absolute;
    left: 641px;
    top: 50px;
    display: flex;
    align-items: center;
    gap: 9px;
  }
  .phone__icon { width: 29px; height: 29px; }
  .phone__number { font-size: 22px; font-weight: 600; line-height: 1; }
  .services {
    position: absolute;
    left: 1017px;
    top: 20px;
    list-style: none;
  }
  .services__item {
    display: flex;
    align-items: center;
    gap: 8px;
    font-size: 15px;
    font-weight: 700;
    line-height: 21.5px;
  }
  .services__item::before {
    content: "";
    width: 6px;
    height: 6px;
    border-radius: 50%;
    background: var(--red);
  }
</style>
</head>
<body>
<div class="banner">
  <svg class="banner__shapes" width="1200" height="100" viewBox="0 0 1200 100">
    <defs>
      <linearGradient id="photoTone" x1="0" y1="0" x2="1" y2="1">
        <stop offset="0" stop-color="var(--photo-mid)"/>
        <stop offset="0.6" stop-color="var(--photo-light)"/>
        <stop offset="1" stop-color="#e6e6e6"/>
      </linearGradient>
      <linearGradient id="redFade" x1="0" y1="0" x2="0" y2="1">
        <stop offset="0" stop-color="var(--red)"/>
        <stop offset="1" stop-color="var(--red-dark)"/>
      </linearGradient>
    </defs>
    <polygon points="0,0 275,0 319,100 0,100" fill="url(#photoTone)" role="img" aria-label="Photo of a red sedan in a bright studio"/>
    <polygon points="286,0 340,0 312,68" fill="url(#redFade)"/>
    <polygon points="1148,0 1200,0 1200,84" fill="url(#redFade)"/>
    <polygon points="1118,100 1151,33 1169,100" fill="url(#redFade)"/>
  </svg>

  <div class="brand">
    <span class="brand__dot"></span>
    <span class="brand__name">KV MOTORS</span>
  </div>

  <p class="tagline">PREMIUM PRE-OWNED VEHICLE SALES</p>

  <div class="phone">
    <svg class="phone__icon" viewBox="0 0 30 30" aria-hidden="true">
      <circle cx="15" cy="15" r="12.5" fill="none" stroke="var(--red)" stroke-width="3"/>
      <path d="M11 8.5c.6-.4 1.3-.3 1.7.3l1.3 2.2c.3.6.2 1.2-.3 1.6l-.9.7c.6 1.5 1.8 2.8 3.3 3.5l.7-.9c.4-.5 1.1-.6 1.6-.3l2.2 1.3c.6.4.7 1.1.3 1.7l-.7 1c-.6.8-1.6 1.1-2.6.8-3.6-1.2-6.3-3.9-7.5-7.5-.3-1 0-2 .8-2.6z" fill="var(--red)"/>
    </svg>
    <span class="phone__number">403.555.0172</span>
  </div>

  <ul class="services">
    <li class="services__item">BUY</li>
    <li class="services__item">SELL</li>
    <li class="services__item">TRADE</li>
  </ul>
</div>
</body>
</html>
```